Velorine Jewellery Display Card

We are a jewellery manufacturer and need artwork for an A4 size strut card to advertise our new "Crescent Loop Pendant "
In the attached files is a picture of the new pendant and artwork for our trademark "Velorine"
We also need to include the phrase " an expression of love "
as part of the artwork.
The background colour should be predominately white

Target Market(s)

This product has been designed as a gift for Mothers as it has their children names
engraved on the pendant

Industry/Entity Type

Manufacturer

Font styles to use
Serif
Script

Colors
ffffff

Requirements
Must have
• Artwork should be simple and elegant , the predominant look in Australian jewellery stores which is where these display cards will be is white, bright and elegant

```html
<!DOCTYPE html>
<html lang="en">
<head>
<meta charset="utf-8">
<title>Velorine – Crescent Loop Pendant</title>
<link href="https://fonts.googleapis.com/css2?family=Great+Vibes&family=Raleway:wght@300;400&display=swap" rel="stylesheet">
<style>
  :root {
    --paper: #ffffff;
    --blush: #f6d9df;
    --blush-soft: #fbeef1;
    --ink-dark: #3f3f42;
    --ink-grey: #a5a7aa;
    --rose: #e47aa3;
    --silver-light: #f4f4f6;
    --silver-mid: #d4d5d9;
    --silver-dark: #a9abb0;
  }
  * { margin: 0; padding: 0; box-sizing: border-box; }
  html, body { width: 1200px; height: 848px; overflow: hidden; }
  body { background: var(--paper); }

  .card {
    position: relative;
    width: 1200px;
    height: 848px;
    overflow: hidden;
    background:
      radial-gradient(ellipse 420px 380px at 0% 20%, var(--blush) 0%, rgba(246,217,223,0) 70%),
      radial-gradient(ellipse 460px 420px at 100% 15%, var(--blush) 0%, rgba(246,217,223,0) 70%),
      radial-gradient(ellipse 520px 360px at 100% 100%, var(--blush-soft) 0%, rgba(251,238,241,0) 75%),
      radial-gradient(ellipse 400px 320px at 0% 100%, var(--blush-soft) 0%, rgba(251,238,241,0) 75%),
      var(--paper);
  }

  .product-title { position: absolute; left: 40px; top: 102px; width: 488px; text-align: right; font-weight: normal; }
  .product-title__script {
    display: block;
    font-family: "Great Vibes", cursive;
    font-size: 96px;
    line-height: 92px;
    color: var(--ink-dark);
  }
  .product-title__caps {
    display: block;
    font-family: "Raleway", sans-serif;
    font-weight: 400;
    font-size: 62px;
    line-height: 62px;
    letter-spacing: 1px;
    color: var(--ink-dark);
  }

  .tagline { position: absolute; left: 40px; top: 374px; width: 526px; text-align: right; }
  .tagline__line {
    display: block;
    font-family: "Raleway", sans-serif;
    font-weight: 300;
    font-size: 64px;
    line-height: 64px;
    letter-spacing: 0.5px;
    color: var(--ink-grey);
  }
  .tagline__line--second {
    display: flex;
    justify-content: flex-end;
    align-items: baseline;
    margin-top: 18px;
    padding-right: 38px;
  }
  .tagline__love {
    font-family: "Great Vibes", cursive;
    font-size: 160px;
    line-height: 64px;
    letter-spacing: 0;
    color: var(--rose);
    margin-left: 34px;
  }

  .pendant-photo {
    position: absolute;
    left: 632px;
    top: 52px;
    width: 480px;
    height: 620px;
  }
  .pendant-photo__bail {
    position: absolute;
    left: 218px; top: 0;
    width: 44px; height: 210px;
    border-radius: 10px 10px 4px 4px;
    background: linear-gradient(90deg, var(--silver-dark), var(--silver-light), var(--silver-dark));
  }
  .pendant-photo__body {
    position: absolute;
    left: 0; top: 120px;
    width: 480px; height: 500px;
    border-radius: 50% 50% 48% 48% / 46% 46% 54% 54%;
    background: radial-gradient(ellipse at 50% 45%, var(--silver-light) 0%, var(--silver-mid) 60%, var(--silver-dark) 100%);
  }

  .brand {
    position: absolute;
    left: 632px; top: 730px;
    width: 482px;
    text-align: right;
    font-family: "Raleway", sans-serif;
    font-weight: 400;
    font-size: 84px;
    line-height: 84px;
    letter-spacing: 1px;
    color: var(--ink-grey);
  }
</style>
</head>
<body>
  <main class="card">
    <h1 class="product-title">
      <span class="product-title__script">Crescent Loop</span>
      <span class="product-title__caps">PENDANT</span>
    </h1>

    <p class="tagline">
      <span class="tagline__line">AN EXPRESSION</span>
      <span class="tagline__line tagline__line--second">OF<span class="tagline__love">love</span></span>
    </p>

    <div class="pendant-photo" role="img" aria-label="Product photo of the silver Crescent Loop Pendant">
      <div class="pendant-photo__bail"></div>
      <div class="pendant-photo__body"></div>
    </div>

    <p class="brand">VELORINE</p>
  </main>
</body>
</html>
```